I need to present the newly formed Cellar Comet concept at a board meeting in 1 weeks time. Cellar Comet is an American gas station Themed dispense concept for wine .. I need a max of 12 page power point template that incorporates a number of the photo elements of the concept and Has the cellar comet logo on each slide .. I have more pics of the concept that I will forward if you accept the project

```html
<!DOCTYPE html>
<html lang="en">
<head>
<meta charset="utf-8">
<title>Cellar Comet – Presentation Template</title>
<link href="https://fonts.googleapis.com/css2?family=Poppins:wght@400;500;600&family=Fira+Sans:ital,wght@1,900&display=swap" rel="stylesheet">
<style>
  :root{
    --page:#3d3d3d;
    --slide:#ffffff;
    --panel:#f3f2f0;
    --panel-edge:#ebe9e6;
    --red:#e3262b;
    --ink:#2a2a2a;
    --body:#4a4a4a;
    --wine-a:#c9a48c;
    --wine-b:#f4ecea;
  }
  *{margin:0;padding:0;box-sizing:border-box}
  html,body{width:1200px;height:4147px;overflow:hidden;background:var(--page)}
  body{position:relative;font-family:"Poppins",sans-serif;color:var(--body)}
  .slide{position:absolute;left:43px;width:1112px;height:625px;background:var(--slide);overflow:hidden}
  .abs{position:absolute}
  .photo{position:absolute}
  .brand{position:absolute;font-family:"Poppins",sans-serif;font-weight:600;color:var(--red);white-space:nowrap;letter-spacing:-.5px}
  .brand--small{right:30px;top:36px;font-size:26px}
  .brand--large{font-size:46px;transform:translateX(-50%)}
  .title{position:absolute;left:31px;top:40px;font-family:"Fira Sans",sans-serif;font-style:italic;font-weight:900;font-size:40px;color:var(--ink);letter-spacing:-.5px;display:flex;align-items:flex-end}
  .title::after{content:"";display:block;width:56px;height:3px;background:var(--red);margin:0 0 9px 12px}
  .rule{position:absolute;height:3px;width:72px;background:var(--red);transform:translateX(-50%)}
  .socials{position:absolute;display:flex;gap:10px;transform:translateX(-50%)}
  .socials span{width:25px;height:25px;border:1.5px solid var(--red);border-radius:50%}
  .lead{font-size:23px;line-height:37px;color:var(--ink);text-align:center}
  .copy{font-size:16.5px;line-height:32.5px;color:var(--body)}
  .bullets{list-style:none}
  .bullets li{position:relative;padding-left:27px;font-size:18.5px;color:var(--ink)}
  .bullets li::before{content:"";position:absolute;left:0;top:11px;width:8px;height:8px;border-radius:50%;background:var(--red)}
  .splash{position:absolute;background:radial-gradient(ellipse at 60% 60%, var(--wine-b) 0%, rgba(255,255,255,0) 70%)}
  .tile{position:absolute;border-radius:8px}
</style>
</head>
<body>

<!-- Cover -->
<section class="slide" style="top:55px">
  <div class="abs" style="left:0;top:0;width:641px;height:625px;background:var(--panel-edge)"></div>
  <div class="abs" role="img" aria-label="Faint line pattern of wine bottles and glasses" style="left:31px;top:29px;width:576px;height:564px;background:var(--panel)"></div>
  <div class="brand brand--large" style="left:335px;top:176px">Cellar Comet</div>
  <p class="abs lead" style="left:60px;top:305px;width:550px">Lorem ipsum dolor sit amet, consecte tur adipiscing elit, sed do eiusmod tempor.</p>
  <div class="rule" style="left:335px;top:416px"></div>
  <div class="socials" style="left:335px;top:456px"><span></span><span></span><span></span></div>
  <div class="photo" role="img" aria-label="Two vintage red and silver fuel pumps under lamps in a dark garage" style="left:641px;top:0;width:471px;height:625px;background:linear-gradient(160deg,#3a2c26 0%,#5b3f31 45%,#2a221f 100%)"></div>
</section>

<!-- Agenda -->
<section class="slide" style="top:733px">
  <h2 class="title">AGENDA</h2>
  <div class="brand brand--small">Cellar Comet</div>
  <div class="splash" role="img" aria-label="Faint wine glass splash" style="left:760px;top:300px;width:352px;height:325px"></div>
  <div class="photo" role="img" aria-label="Row of colourful vintage fuel pumps against a concrete wall" style="left:0;top:116px;width:501px;height:509px;background:linear-gradient(100deg,#2f3d6b 0%,#d8672a 40%,#e5c23a 62%,#3b3a38 85%,#9a9286 100%)"></div>
  <div class="abs" style="left:501px;top:145px;width:17px;height:480px;background:var(--red)"></div>
  <p class="abs copy" style="left:583px;top:140px;width:500px;font-size:18px;line-height:33px;color:var(--ink)">Lorem ipsum dolor sit amet, consecte tur adipiscing elit, sed do eiusmod tempor.</p>
  <ul class="abs bullets" style="left:583px;top:250px">
    <li style="margin-bottom:25px">Introduction</li>
    <li style="margin-bottom:25px">Why Choose Us</li>
    <li style="margin-bottom:25px">Review</li>
    <li style="margin-bottom:25px">Gallery</li>
    <li>Thank You</li>
  </ul>
</section>

<!-- About us -->
<section class="slide" style="top:1413px">
  <h2 class="title">ABOUT US</h2>
  <div class="brand brand--small">Cellar Comet</div>
  <div class="splash" role="img" aria-label="Faint wine glass splash" style="left:800px;top:230px;width:312px;height:220px"></div>
  <div class="abs copy" style="left:31px;top:123px;width:500px">
    <p>Lorem ipsum dolor sit amet, consectetur adipisg elit, sed do eiusmod tempor incididnt ut labore et dolore magna aliqua. Ut enim ad minim veniam, quis nostrexercitation ullamco laboris nisi ut aliquip ex ea immodo consequat. Duis aute irure dolor in reprehierit in voluptate velit esse cillum dolore eu fugiait nulla pariatur.</p>
    <p style="margin-top:8px">Ipsum dolor sit amet, consectetur adipisg elit, seiusmod tempor incididnt ut labore et dolore magna aliqua.</p>
  </div>
  <div class="abs copy" style="left:577px;top:123px;width:505px">
    <p>Lorem ipsum dolor sit amet, consectetur adipisg elit, sed do eiusmod tempor incididnt ut labore et dolore magna aliqua.</p>
    <p style="margin-top:8px">Ut enim ad minim veniam, quis nostrexercitation uamco laboris nisi ut aliquip ex ea immodo consquat. Duis aute irure dolor in reprehierit in voluptate vesse cillum dolore eu fugiait nulla pariatur.</p>
  </div>
  <div class="abs" style="left:31px;top:438px;width:1050px;height:187px;border:1.5px solid var(--red);border-bottom:none"></div>
  <div class="photo" role="img" aria-label="Row of wine glasses filled with rosé wine in warm light" style="left:0;top:449px;width:1112px;height:176px;background:linear-gradient(90deg,#2b1d1a 0%,#c77a45 22%,#3a2a28 45%,#1e2630 70%,#6b3a2c 100%)"></div>
</section>

<!-- Why us -->
<section class="slide" style="top:2091px">
  <h2 class="title">WHY US</h2>
  <div class="brand brand--small">Cellar Comet</div>
  <div class="splash" role="img" aria-label="Faint wine glass splash" style="left:760px;top:340px;width:352px;height:285px"></div>
  <ul class="abs bullets" style="left:31px;top:152px;width:400px">
    <li class="copy" style="font-size:17.5px;line-height:32.5px;color:var(--body);margin-bottom:77px">Lorem ipsum dolor sit amet, consectetur adip isg elit, sed do eiusmod tempr incit ut labore et dolore magna aliqua.</li>
    <li class="copy" style="font-size:17.5px;line-height:32.5px;color:var(--body)">Lorem ipsum dolor sit amet, consectetur adip isg elit, sed do eiusmod tempr incit ut labore et dolore magna aliqua.</li>
  </ul>
  <div class="photo" role="img" aria-label="Single red vintage fuel pump with a round globe on top" style="left:456px;top:108px;width:209px;height:451px;border-radius:40px 40px 12px 12px;background:linear-gradient(180deg,#f0e3d6 0%,#d8302c 22%,#c8242a 80%,#3a3a3a 100%)"></div>
  <ul class="abs bullets" style="left:702px;top:246px;width:400px">
    <li class="copy" style="font-size:17.5px;line-height:32.5px;color:var(--body);margin-bottom:77px">Lorem ipsum dolor sit amet, consectetur adip isg elit, sed do eiusmod tempr incit ut labore et dolore magna aliqua.</li>
    <li class="copy" style="font-size:17.5px;line-height:32.5px;color:var(--body)">Lorem ipsum dolor sit amet, consectetur adip isg elit, sed do eiusmod tempr incit ut labore et dolore magna aliqua.</li>
  </ul>
</section>

<!-- Gallery -->
<section class="slide" style="top:2771px">
  <h2 class="title">GALLERY</h2>
  <div class="brand brand--small">Cellar Comet</div>
  <div class="splash" role="img" aria-label="Faint wine glass splash" style="left:780px;top:330px;width:332px;height:295px"></div>
  <div class="tile" role="img" aria-label="Two cream and red vintage fuel pumps in a showroom" style="left:55px;top:132px;width:319px;height:404px;background:linear-gradient(135deg,#2c5a86 0%,#e9e4cf 45%,#c84034 70%,#3d4f6a 100%)"></div>
  <div class="tile" role="img" aria-label="Restored silver and red fuel pumps beside a display of cans" style="left:396px;top:132px;width:318px;height:195px;background:linear-gradient(120deg,#d9d6d1 0%,#8a8886 40%,#c8322c 75%,#e6e2dc 100%)"></div>
  <div class="tile" role="img" aria-label="Fuel pumps under lamps in a dark garage" style="left:396px;top:341px;width:318px;height:195px;background:linear-gradient(120deg,#2e2420 0%,#6b4a36 45%,#a83a2c 65%,#2a2220 100%)"></div>
  <div class="tile" role="img" aria-label="Red and white fuel pumps under a lamp in a bright showroom" style="left:736px;top:132px;width:320px;height:404px;background:linear-gradient(160deg,#eeeae4 0%,#d23a2e 40%,#f3f1ec 60%,#3d6b3e 85%,#d9d4cc 100%)"></div>
</section>

<!-- Thank you -->
<section class="slide" style="top:3451px">
  <div class="photo" role="img" aria-label="Turquoise and cream vintage fuel pump in front of a blurred warm bar interior" style="left:0;top:0;width:470px;height:625px;background:linear-gradient(120deg,#3a2014 0%,#8a4a22 35%,#2f9a92 55%,#e8e1cc 70%,#5a3018 100%)"></div>
  <div class="abs" style="left:470px;top:0;width:642px;height:625px;background:var(--panel-edge)"></div>
  <div class="abs" role="img" aria-label="Faint line pattern of wine bottles and glasses" style="left:499px;top:29px;width:582px;height:567px;background:var(--panel)"></div>
  <div class="brand brand--large" style="left:794px;top:174px">Cellar Comet</div>
  <div class="abs" style="left:794px;top:298px;transform:translateX(-50%);font-family:'Fira Sans',sans-serif;font-style:italic;font-weight:900;font-size:60px;color:var(--ink);white-space:nowrap">Thank you</div>
  <div class="rule" style="left:794px;top:389px"></div>
  <div class="socials" style="left:794px;top:425px"><span></span><span></span><span></span></div>
</section>

</body>
</html>
```